Quillo Business Card Design

Looking for elegant and super stylish business cards. Enclosed is the card design we are using now. We need something more contemporary.

Target Market(s)

We are a catering company focusing on weddings and corporate events.

Industry/Entity Type

Caterer

Contact Information for Business Card

Please use similar font to our current cards

Colors
0592cd

Requirements
Must have
• Color and be very unique. Also, please use logo (with or without the castle.)

```html
<!DOCTYPE html>
<html lang="en">
<head>
<meta charset="utf-8">
<title>Quillo Business Card Design</title>
<link rel="stylesheet" href="https://fonts.googleapis.com/css2?family=EB+Garamond:ital,wght@0,400;1,400&family=Roboto:ital,wght@0,400;0,700;1,400;1,700&display=swap">
<style>
  :root {
    --brand-blue: #0592cd;
    --ink: #1a1f24;
    --muted-ink: #3a3f44;
    --paper: #ffffff;
    --backdrop: #eef0f2;
    --pattern-light: #f7f7f8;
    --pattern-dark: #ebecee;
  }
  * { box-sizing: border-box; margin: 0; padding: 0; }
  html, body { width: 1200px; height: 863px; overflow: hidden; }
  body {
    background: var(--backdrop);
    display: flex;
    align-items: center;
    justify-content: center;
    gap: 80px;
  }
  .card {
    position: relative;
    width: 340px;
    height: 580px;
    background: var(--paper);
    box-shadow: 0 6px 24px rgba(0,0,0,0.12);
    overflow: hidden;
  }
  .card-corners { position: absolute; inset: 0; width: 100%; height: 100%; }
  .card-texture {
    position: absolute;
    inset: 60px 0 60px 0;
    background: linear-gradient(160deg, var(--pattern-light) 0%, var(--pattern-dark) 50%, var(--pattern-light) 100%);
  }

  /* Back of card */
  .card-back .services {
    position: absolute;
    top: 80px;
    right: 40px;
    left: 40px;
    text-align: right;
  }
  .services-title {
    font-family: "EB Garamond", serif;
    font-style: italic;
    font-size: 26px;
    line-height: 1.0;
    color: var(--muted-ink);
  }
  .services-rule {
    height: 4px;
    background: var(--brand-blue);
    margin: 14px 0 14px;
  }
  .services-note {
    font-family: "Roboto", sans-serif;
    font-style: italic;
    font-size: 13px;
    color: var(--muted-ink);
  }
  .services-tagline {
    font-family: "Roboto", sans-serif;
    font-style: italic;
    font-weight: 700;
    font-size: 14px;
    color: var(--ink);
    margin-top: 2px;
  }

  /* Front of card */
  .brand {
    position: absolute;
    top: 72px;
    left: 0;
    right: 0;
    display: flex;
    align-items: center;
    justify-content: center;
    gap: 10px;
  }
  .brand-square { width: 34px; height: 34px; background: var(--ink); }
  .brand-name {
    font-family: "Roboto", sans-serif;
    font-weight: 400;
    font-size: 24px;
    letter-spacing: 1px;
    color: var(--ink);
  }
  .person {
    position: absolute;
    top: 210px;
    left: 0;
    right: 0;
    text-align: center;
  }
  .person-name {
    font-family: "Roboto", sans-serif;
    font-weight: 700;
    font-size: 26px;
    color: var(--ink);
  }
  .person-title {
    font-family: "EB Garamond", serif;
    font-style: italic;
    font-size: 18px;
    color: var(--muted-ink);
  }
  .divider {
    width: 70px;
    height: 2px;
    background: var(--ink);
    margin: 34px auto 0;
  }
  .contact {
    position: absolute;
    top: 350px;
    left: 0;
    right: 0;
    text-align: center;
    font-family: "Roboto", sans-serif;
    font-size: 14px;
    line-height: 1.35;
    color: var(--ink);
  }
  .contact-group + .contact-group { margin-top: 12px; }
</style>
</head>
<body>

  <section class="card card-back" aria-label="Business card back">
    <div class="card-texture" role="img" aria-label="Faint diagonal line pattern across the card"></div>
    <svg class="card-corners" viewBox="0 0 340 580" aria-hidden="true">
      <polygon points="0,0 70,0 0,45" fill="var(--brand-blue)"/>
      <polygon points="340,580 270,580 340,535" fill="var(--brand-blue)"/>
    </svg>
    <div class="services">
      <p class="services-title">Catering<br>Event Design</p>
      <div class="services-rule"></div>
      <p class="services-note">All-inclusive Packages</p>
      <p class="services-tagline">Gourmet Events. Skinny Prices.</p>
    </div>
  </section>

  <section class="card card-front" aria-label="Business card front">
    <div class="card-texture" role="img" aria-label="Faint diagonal line pattern across the card"></div>
    <svg class="card-corners" viewBox="0 0 340 580" aria-hidden="true">
      <polygon points="0,0 70,0 0,45" fill="var(--brand-blue)"/>
      <polygon points="340,580 270,580 340,535" fill="var(--brand-blue)"/>
    </svg>
    <div class="brand">
      <span class="brand-square"></span>
      <span class="brand-name">THE QUILLO</span>
    </div>
    <div class="person">
      <p class="person-name">Marlo Vestin</p>
      <p class="person-title">Chief Executive Officer</p>
      <div class="divider"></div>
    </div>
    <div class="contact">
      <div class="contact-group">
        <p>Office: 555 014 2290 ext. 312</p>
        <p>Fax: 555 014 7731</p>
      </div>
      <div class="contact-group">
        <p>4120 Harbor Lane</p>
        <p>Bayview, California 90000</p>
      </div>
      <div class="contact-group">
        <p>m@TheQuilloCatering.com</p>
        <p>www.TheQuilloCatering.com</p>
      </div>
    </div>
  </section>

</body>
</html>
```